Design for an iOS and Android app managing shopping list

The app allows you to keep manage shopping lists, each shopping list being made of items to buy...
We need a design for the 3 screens of the app:
a) global view showing list of (shopping) list
b) form enabling to edit the name of a (shopping) list
c) detailed view listing the contents/items of a (shopping) list
d) 1 text page [not illustrated]
2 "alerts" items are also to be designed: confirm and error pop ups.
No specific guidelines, nor logo or whatever.
It will be a free app distributed on iOS and Androïd.
We just want to make it looking nice & very usable for end users.

```html
<!DOCTYPE html>
<html lang="en">
<head>
<meta charset="utf-8">
<title>Shopping List App Screens</title>
<link rel="stylesheet" href="https://fonts.googleapis.com/css2?family=Open+Sans:wght@400&family=Inter:wght@400;500;600&display=swap">
<style>
:root{
  --panel-left:#465869;
  --panel-right:#3e7198;
  --gap:#ffffff;
  --title:#111418;
  --screen:#ffffff;
  --bar:#f7f7f7;
  --ink:#1d1d1f;
  --muted:#7b7b80;
  --accent:#1f8fe0;
  --band:#1d9ae3;
  --rule:#e3e3e6;
  --gray-gap:#e9e9ec;
  --strike:#e0322c;
  --battery:#3cc83c;
}
*{box-sizing:border-box;margin:0;padding:0}
html,body{width:1200px;height:1053px;overflow:hidden;background:var(--gap)}
body{position:relative;font-family:"Inter",sans-serif;color:var(--ink)}
.panel{position:absolute;top:0;height:1053px}
.panel--list{left:0;width:592px;background:var(--panel-left)}
.panel--overview{left:608px;width:592px;background:var(--panel-right)}
.panel__title{position:absolute;top:22px;left:0;width:100%;text-align:center;font-family:"Open Sans",sans-serif;font-size:41px;line-height:80px;color:var(--title)}
.screen{position:absolute;top:380px;left:58px;width:474px;height:673px;background:var(--screen);overflow:hidden}
.panel--overview .screen{left:60px;width:470px}
.status{position:absolute;top:0;left:0;width:100%;height:30px;font-size:13px;font-weight:500;color:#111}
.status span{position:absolute;top:7px}
.status__carrier{left:10px}
.status__time{left:0;width:100%;text-align:center}
.status__right{right:12px;display:flex;align-items:center;gap:4px}
.battery{display:inline-block;width:28px;height:11px;border:1px solid #999;border-radius:2px;padding:1px}
.battery i{display:block;width:100%;height:100%;background:var(--battery);border-radius:1px}
.nav{position:absolute;top:30px;left:0;width:100%;height:52px;background:var(--bar)}
.nav__back{position:absolute;left:14px;top:12px;font-size:20px;color:var(--accent);display:flex;align-items:center;gap:4px}
.nav__title{position:absolute;top:14px;width:100%;text-align:center;font-size:19px;font-weight:500}
.nav__icon{position:absolute;top:12px}
.abs{position:absolute}
.add-item{position:absolute;left:14px;top:92px;width:448px;height:44px;border:1px solid var(--rule);border-radius:4px;text-align:center;line-height:42px;font-size:20px;color:var(--accent)}
.list-head{position:absolute;top:146px;left:0;width:100%;height:92px;border-top:1px solid var(--rule)}
.list-head__name{position:absolute;left:20px;top:8px;font-size:25px;font-weight:500}
.list-head__count{position:absolute;left:20px;top:42px;font-size:17px;color:var(--muted)}
.list-head__toggle{position:absolute;left:20px;top:66px;font-size:17px;font-weight:600;color:var(--accent)}
.cell-divider{position:absolute;left:385px;width:1px;background:var(--rule)}
.band{position:absolute;left:0;width:100%;background:var(--band);color:#fff;font-size:17px;font-weight:600;display:flex;align-items:center;justify-content:center;gap:6px}
.item{position:absolute;left:0;width:100%;border-bottom:1px solid var(--rule)}
.item__name{position:absolute;left:20px;font-size:20px}
.item__note{position:absolute;left:20px;font-size:16px;color:var(--muted);display:flex;align-items:center;gap:6px}
.item__name--done{text-decoration:line-through;text-decoration-color:var(--strike);text-decoration-thickness:2px;color:#555}
.item__photo{position:absolute;left:20px;top:6px;width:76px;height:50px;background:linear-gradient(135deg,#d9d9d4,#6f8a45 40%,#3c5a24 70%,#c9c9c2)}
.edit{position:absolute;right:24px}
.gray-gap{position:absolute;left:0;width:100%;background:var(--gray-gap)}
.row{position:absolute;left:0;width:100%;border-bottom:1px solid var(--rule)}
.row__icon{position:absolute;left:22px}
.row__name{position:absolute;left:72px;font-size:20px}
.row__sub{position:absolute;left:72px;font-size:16px;color:var(--muted);display:flex;align-items:center;gap:5px}
.row__chev{position:absolute;left:346px}
.row__gear{position:absolute;left:414px}
.row-divider{position:absolute;left:382px;width:1px;background:var(--rule)}
.create{position:absolute;left:0;top:590px;width:100%;height:52px;text-align:center;line-height:52px;font-size:20px;color:var(--accent);background:#fff}
.signed{position:absolute;left:0;top:642px;width:100%;height:31px;text-align:center;font-size:15px;font-style:italic;color:var(--muted);background:var(--gray-gap);line-height:42px}
</style>
</head>
<body>
<svg width="0" height="0" style="position:absolute">
  <defs>
    <symbol id="gear" viewBox="0 0 24 24">
      <circle cx="12" cy="12" r="7.5" fill="none" stroke="#1f8fe0" stroke-width="5" stroke-dasharray="3.2 2.7"/>
      <circle cx="12" cy="12" r="6.5" fill="#1f8fe0"/>
      <circle cx="12" cy="12" r="2.8" fill="#fff"/>
    </symbol>
    <symbol id="pencil" viewBox="0 0 40 30">
      <path d="M14 22 L31 5 L35 9 L18 26 L12 28 Z" fill="#1f8fe0"/>
      <line x1="2" y1="27" x2="14" y2="27" stroke="#e0322c" stroke-width="1.2"/>
    </symbol>
    <symbol id="doc" viewBox="0 0 26 34">
      <path d="M3 3 L23 1 L23 33 L3 31 Z" fill="none" stroke="currentColor" stroke-width="3.5" stroke-linejoin="round"/>
      <line x1="8" y1="11" x2="18" y2="10" stroke="currentColor" stroke-width="2.5"/>
      <line x1="8" y1="17" x2="18" y2="17" stroke="currentColor" stroke-width="2.5"/>
      <line x1="8" y1="23" x2="18" y2="24" stroke="currentColor" stroke-width="2.5"/>
    </symbol>
    <symbol id="folder" viewBox="0 0 34 28">
      <path d="M1 4 Q1 2 3 2 L12 2 L15 5 L31 5 Q33 5 33 7 L33 26 L1 26 Z" fill="currentColor"/>
      <rect x="1" y="8" width="32" height="18" fill="currentColor" opacity=".85"/>
    </symbol>
    <symbol id="chev" viewBox="0 0 10 18"><path d="M2 2 L8 9 L2 16" fill="none" stroke="#b5b5ba" stroke-width="1.8"/></symbol>
  </defs>
</svg>

<section class="panel panel--list">
  <h2 class="panel__title">Global view showing list of<br>(shopping) list</h2>
  <div class="screen">
    <div class="status"><span class="status__carrier">●●●●○ Nova</span><span class="status__time">12:38 PM</span><span class="status__right">99% <b class="battery"><i></i></b></span></div>
    <div class="nav">
      <div class="nav__back"><svg width="12" height="22" viewBox="0 0 12 22"><path d="M10 2 L2 11 L10 20" fill="none" stroke="#1f8fe0" stroke-width="2.5"/></svg>Lists</div>
      <svg class="nav__icon" style="left:234px" width="28" height="28" viewBox="0 0 24 24"><path d="M12 2 L14.9 8.6 L22 9.3 L16.6 14 L18.2 21 L12 17.3 L5.8 21 L7.4 14 L2 9.3 L9.1 8.6 Z" fill="none" stroke="#1f8fe0" stroke-width="1.6" stroke-linejoin="round"/></svg>
      <svg class="nav__icon" style="left:298px" width="28" height="28" viewBox="0 0 24 24"><circle cx="12" cy="12" r="9.5" fill="none" stroke="#1f8fe0" stroke-width="1.8"/><path d="M12 6 L12 12 L8 12" fill="none" stroke="#1f8fe0" stroke-width="1.8"/></svg>
      <svg class="nav__icon" style="left:362px" width="28" height="28" viewBox="0 0 24 24"><path d="M3 4 L21 4 L14 12 L14 20 L10 18 L10 12 Z" fill="none" stroke="#1f8fe0" stroke-width="1.8" stroke-linejoin="round"/><line x1="5.5" y1="7" x2="18.5" y2="7" stroke="#1f8fe0" stroke-width="1.4"/></svg>
      <svg class="nav__icon" style="left:424px;top:20px" width="30" height="10" viewBox="0 0 30 10"><circle cx="5" cy="5" r="3.5" fill="#1f8fe0"/><circle cx="15" cy="5" r="3.5" fill="#1f8fe0"/><circle cx="25" cy="5" r="3.5" fill="#1f8fe0"/></svg>
    </div>
    <div class="add-item">+ Add Item</div>
    <div class="list-head">
      <div class="list-head__name">Shared Grocery List</div>
      <div class="list-head__count">4 of 5 items remaining</div>
      <div class="list-head__toggle">Hide Completed Items</div>
      <svg class="abs" style="left:412px;top:30px" width="34" height="34"><use href="#gear"/></svg>
    </div>
    <div class="cell-divider" style="top:148px;height:90px"></div>

    <div class="band" style="top:238px;height:38px"><svg width="18" height="14" viewBox="0 0 18 14"><path d="M1 6 L9 1 L17 5 L17 12 L1 13 Z" fill="#fff"/></svg>Dairy</div>
    <div class="item" style="top:276px;height:60px"><div class="item__name" style="top:16px">Eggs</div><svg class="edit" style="top:14px" width="40" height="30"><use href="#pencil"/></svg></div>

    <div class="band" style="top:336px;height:36px"><svg width="20" height="12" viewBox="0 0 20 12"><path d="M1 11 Q3 3 10 2 Q18 1 19 7 Q18 11 12 11 Z" fill="#fff"/></svg>Meat</div>
    <div class="item" style="top:372px;height:62px"><div class="item__name" style="top:6px">Ground Beef</div><div class="item__note" style="top:34px"><svg width="14" height="18" viewBox="0 0 14 18"><path d="M2 1 L2 17 M5 1 L5 17 M10 1 Q13 4 10 9 L10 17" stroke="#1f8fe0" stroke-width="2" fill="none"/></svg>2 lbs for Meatloaf</div><svg class="edit" style="top:18px" width="40" height="30"><use href="#pencil"/></svg></div>

    <div class="band" style="top:434px;height:36px"><svg width="14" height="16" viewBox="0 0 14 16"><path d="M7 4 Q13 1 13 8 Q12 15 7 14 Q2 15 1 8 Q1 1 7 4 Z" fill="#fff"/></svg>Produce</div>
    <div class="item" style="top:470px;height:58px"><div class="item__name item__name--done" style="top:14px">Apples</div><svg class="edit" style="top:14px" width="40" height="30"><use href="#pencil"/></svg></div>
    <div class="item" style="top:528px;height:62px"><div class="item__photo" role="img" aria-label="Photo of a head of broccoli"></div><div class="item__name" style="top:18px;left:106px">Broccoli</div><svg class="edit" style="top:16px" width="40" height="30"><use href="#pencil"/></svg></div>

    <div class="band" style="top:590px;height:36px"><svg width="20" height="10" viewBox="0 0 20 10"><path d="M1 5 Q7 0 14 5 L19 1 L19 9 L14 5 Q7 10 1 5 Z" fill="#fff"/></svg>Seafood</div>
    <div class="item" style="top:626px;height:60px;border:0"><div class="item__name" style="top:8px">Salmon</div><div class="item__note" style="top:36px">Harbor Market</div><svg class="edit" style="top:20px" width="40" height="30"><use href="#pencil"/></svg></div>
  </div>
</section>

<section class="panel panel--overview">
  <h2 class="panel__title">Enabling to edit the<br>name of a (shopping) list</h2>
  <div class="screen">
    <div class="status"><span class="status__carrier">●●●●○ Nova</span><span class="status__time">12:38 PM</span><span class="status__right">99% <b class="battery"><i></i></b></span></div>
    <div class="nav" style="border-bottom:1px solid var(--rule)">
      <div class="nav__title">Lists</div>
      <svg class="nav__icon" style="left:424px;top:20px" width="30" height="10" viewBox="0 0 30 10"><circle cx="5" cy="5" r="3.5" fill="#1f8fe0"/><circle cx="15" cy="5" r="3.5" fill="#1f8fe0"/><circle cx="25" cy="5" r="3.5" fill="#1f8fe0"/></svg>
    </div>
    <div class="gray-gap" style="top:82px;height:44px"></div>

    <div class="row" style="top:126px;height:82px">
      <svg class="row__icon" style="top:22px;color:#1f8fe0" width="26" height="34"><use href="#doc"/></svg>
      <div class="row__name" style="top:8px">Shared Grocery List</div>
      <div class="row__sub" style="top:34px">4 items remaining</div>
      <div class="row__sub" style="top:56px"><svg width="18" height="14" viewBox="0 0 18 14"><circle cx="6" cy="4" r="3" fill="#1f8fe0"/><circle cx="12" cy="4" r="3" fill="#1f8fe0"/><path d="M0 14 Q6 5 12 14 Z M8 14 Q12 6 18 14 Z" fill="#1f8fe0"/></svg>Dana Kole</div>
      <svg class="row__gear" style="top:27px" width="28" height="28"><use href="#gear"/></svg>
    </div>
    <div class="row" style="top:208px;height:62px">
      <svg class="row__icon" style="top:14px;color:#5b4fd0" width="26" height="34"><use href="#doc"/></svg>
      <div class="row__name" style="top:8px">To Do</div>
      <div class="row__sub" style="top:34px">1 item remaining</div>
      <svg class="row__gear" style="top:17px" width="28" height="28"><use href="#gear"/></svg>
    </div>
    <div class="row" style="top:270px;height:64px">
      <svg class="row__icon" style="top:15px;color:#e5392c" width="26" height="34"><use href="#doc"/></svg>
      <div class="row__name" style="top:8px">Gift Ideas</div>
      <div class="row__sub" style="top:34px">3 items</div>
      <svg class="row__gear" style="top:18px" width="28" height="28"><use href="#gear"/></svg>
    </div>
    <div class="row" style="top:334px;height:62px">
      <svg class="row__icon" style="top:14px;color:#1f8fe0" width="26" height="34"><use href="#doc"/></svg>
      <div class="row__name" style="top:6px">Movies to Watch</div>
      <div class="row__sub" style="top:32px">10 items</div>
      <svg class="row__gear" style="top:17px" width="28" height="28"><use href="#gear"/></svg>
    </div>
    <div class="row" style="top:396px;height:56px">
      <svg class="row__icon" style="top:14px;left:18px;color:#2b9be8" width="34" height="28"><use href="#folder"/></svg>
      <div class="row__name" style="top:15px">Shopping</div>
      <svg class="row__chev" style="top:19px" width="10" height="18"><use href="#chev"/></svg>
      <svg class="row__gear" style="top:14px" width="28" height="28"><use href="#gear"/></svg>
    </div>
    <div class="row" style="top:452px;height:54px">
      <svg class="row__icon" style="top:13px;left:18px;color:#28c93a" width="34" height="28"><use href="#folder"/></svg>
      <div class="row__name" style="top:14px">Travel</div>
      <svg class="row__chev" style="top:18px" width="10" height="18"><use href="#chev"/></svg>
      <svg class="row__gear" style="top:13px" width="28" height="28"><use href="#gear"/></svg>
    </div>
    <div class="row" style="top:506px;height:56px;border:0">
      <svg class="row__icon" style="top:14px;left:18px;color:#8e8e93" width="34" height="28"><use href="#folder"/></svg>
      <div class="row__name" style="top:15px">Archive</div>
      <svg class="row__chev" style="top:19px" width="10" height="18"><use href="#chev"/></svg>
      <svg class="row__gear" style="top:14px" width="28" height="28"><use href="#gear"/></svg>
    </div>
    <div class="row-divider" style="top:126px;height:436px"></div>

    <div class="gray-gap" style="top:562px;height:28px"></div>
    <div class="create">Create a new list</div>
    <div class="signed">Signed in as sam@listmail.app</div>
  </div>
</section>
</body>
</html>
```